Rack Card Design Project

We are a locally family owned public golf course. We would like to have a rack card designed that can be used for multiple applications. The colors in our logo are grey, blue, and white. Please use those in the card design. The company logo, contact information, address, and summer pricing should be included. I've included some pictures that may or may not be used. I'm also open to suggestions....use one photo, multiple photos, a stock photo or image representing golf etc.

```html
<!DOCTYPE html>
<html lang="en">
<head>
<meta charset="utf-8">
<title>Cedar Creek Golf Club Rack Card</title>
<link rel="stylesheet" href="https://fonts.googleapis.com/css2?family=Montserrat:wght@400;500;700;800&family=Playfair+Display:wght@700;900&display=swap">
<style>
  :root {
    --navy: #15305a;
    --grey: #8d8e90;
    --grey-light: #a7a9ac;
    --rate-muted: #c3c9d6;
    --white: #ffffff;
    --page: #e4e5e7;
    --serif: "Playfair Display", Georgia, serif;
    --sans: "Montserrat", Arial, sans-serif;
  }
  * { box-sizing: border-box; margin: 0; padding: 0; }
  html, body { width: 1143px; height: 1200px; overflow: hidden; }
  body { background: var(--page); position: relative; font-family: var(--sans); }

  .card { position: absolute; top: 31px; width: 504px; height: 1078px; background: var(--white); overflow: hidden; }
  .card--front { left: 39px; }
  .card--back { left: 583px; }

  .side-label { position: absolute; top: 1135px; width: 504px; text-align: center; font: 800 40px var(--sans); color: #111; letter-spacing: 1px; }
  .side-label--front { left: 39px; }
  .side-label--back { left: 583px; }

  .top-rule { position: absolute; left: 0; right: 0; top: 97px; height: 6px; background: var(--navy); }

  .hero-photo { position: absolute; left: 0; right: 0; top: 103px; height: 495px;
    background: linear-gradient(180deg, #4f8e34 0%, #6aa548 45%, #8cc15d 70%, #9fcc6a 100%); }

  .badge { position: absolute; left: 114px; top: 22px; width: 276px; height: 276px; border-radius: 50%;
    background: var(--white); display: flex; align-items: center; justify-content: center; text-align: center; }
  .badge-name { font: 700 30px/1.15 var(--serif); color: var(--navy); width: 200px; }

  .welcome { position: absolute; left: 0; right: 0; top: 608px; text-align: center; font-family: var(--serif); font-weight: 700; color: var(--navy); }
  .welcome-lead { font-size: 50px; color: var(--grey); line-height: 56px; letter-spacing: 1px; }
  .welcome-name { font-size: 34px; line-height: 40px; }

  .photo-band { position: absolute; left: 0; right: 0; bottom: 64px; background: var(--navy); border-top: 6px solid var(--grey-light); }
  .card--front .photo-band { top: 779px; }
  .card--back .rates-panel { position: absolute; left: 0; right: 0; top: 103px; height: 607px; background: var(--navy); }
  .card--back .photo-band { top: 712px; bottom: 64px; }

  .photo-row { position: absolute; left: 0; right: 0; display: flex; justify-content: center; gap: 21px; }
  .card--front .photo-row { top: 769px; }
  .card--back .photo-row { top: 702px; }
  .circle-photo { width: 138px; height: 138px; border-radius: 50%; border: 6px solid var(--grey-light); }
  .circle-photo--inner { border-color: var(--navy); box-shadow: 0 0 0 6px var(--grey-light); }

  .tone-course { background: linear-gradient(180deg, #8cc3ea 0%, #4f8a3e 45%, #79b24c 100%); }
  .tone-palms { background: linear-gradient(180deg, #a9d0ef 0%, #3f6e35 55%, #6e9a44 100%); }
  .tone-dawn { background: linear-gradient(180deg, #e2c48c 0%, #a98a52 55%, #6e6a3a 100%); }
  .tone-bag { background: linear-gradient(135deg, #1b3a24 0%, #3b5e3a 50%, #c9ccd0 100%); }
  .tone-trees { background: linear-gradient(180deg, #c9b89a 0%, #6e6a4a 55%, #4d5a32 100%); }
  .tone-swing { background: linear-gradient(180deg, #8fc26a 0%, #2fa2c6 60%, #6aa548 100%); }

  .contact { position: absolute; left: 0; right: 0; top: 914px; text-align: center; color: var(--white); }
  .contact-call { font: 800 34px var(--sans); display: flex; justify-content: center; align-items: center; gap: 10px; }
  .contact-call .phone-number { font-weight: 700; letter-spacing: 1px; }
  .contact-web { font: 400 32px var(--sans); margin-top: 2px; }

  .footer { position: absolute; left: 0; right: 0; bottom: 0; height: 62px; background: var(--grey);
    border-top: 4px solid var(--white); color: var(--white); font: 500 15.5px/1.4 var(--sans);
    display: flex; align-items: center; justify-content: center; text-align: center; }

  .rates-title { position: absolute; left: 0; right: 0; top: 300px; text-align: center; color: var(--white); font-family: var(--serif); font-weight: 700; }
  .rates-title h2 { font-size: 60px; line-height: 1; letter-spacing: 1px; font-weight: 700; }
  .rates-title p { font-size: 38px; line-height: 1.3; }

  .rate-list { position: absolute; left: 0; right: 0; top: 440px; list-style: none; text-align: center; color: var(--white); font: 800 28px/39.5px var(--sans); }
  .rate-muted { color: var(--rate-muted); }

  .notes { position: absolute; left: 0; right: 0; top: 850px; text-align: center; color: var(--white); font: 800 29px/1.1 var(--sans); }
  .notes .regular { font-weight: 500; }
  .notes p + p { margin-top: 14px; }
</style>
</head>
<body>

  <section class="card card--front">
    <div class="hero-photo" role="img" aria-label="Golfer in a blue shirt finishing a drive on a green fairway lined with trees"></div>
    <div class="top-rule"></div>
    <div class="badge"><span class="badge-name">Cedar Creek Golf Club</span></div>

    <div class="welcome">
      <div class="welcome-lead">Welcome to The</div>
      <div class="welcome-name">Harbors of Cedar Creek<br>Golf Club</div>
    </div>

    <div class="photo-band"></div>
    <div class="photo-row">
      <div class="circle-photo tone-course" role="img" aria-label="Fairway with bunker and trees"></div>
      <div class="circle-photo circle-photo--inner tone-palms" role="img" aria-label="Palm trees beside a green"></div>
      <div class="circle-photo tone-dawn" role="img" aria-label="Flagstick on a misty green at sunrise"></div>
    </div>

    <div class="contact">
      <div class="contact-call">
        <span>CALL US</span>
        <svg width="28" height="28" viewBox="0 0 24 24" aria-hidden="true"><path fill="#ffffff" d="M6.6 10.8a15.1 15.1 0 0 0 6.6 6.6l2.2-2.2c.3-.3.7-.4 1-.2 1.1.4 2.3.6 3.6.6.6 0 1 .4 1 1V20c0 .6-.4 1-1 1A17 17 0 0 1 3 4c0-.6.4-1 1-1h3.5c.6 0 1 .4 1 1 0 1.3.2 2.5.6 3.6.1.3 0 .7-.2 1z"/></svg>
        <span class="phone-number">555-014-2738</span>
      </div>
      <div class="contact-web">www.cedarcreekgc.com</div>
    </div>

    <footer class="footer">The Harbors of Cedar Creek Golf Club 4410 SW<br>Heron Bay Dr Palmview, FL 30000</footer>
  </section>

  <section class="card card--back">
    <div class="rates-panel"></div>
    <div class="top-rule"></div>
    <div class="badge"><span class="badge-name">Cedar Creek Golf Club</span></div>

    <div class="rates-title">
      <h2>Summer Rates</h2>
      <p>May 1-September 30</p>
    </div>

    <ul class="rate-list">
      <li class="rate-muted">18 Holes With Cart</li>
      <li>7AM-11AM $24</li>
      <li>11AM-3PM $19</li>
      <li>3PM-Close $15</li>
      <li><span class="rate-muted">9 Holes With Cart-</span>$15</li>
      <li>Walking $12</li>
    </ul>

    <div class="photo-band"></div>
    <div class="photo-row">
      <div class="circle-photo tone-bag" role="img" aria-label="Golf clubs in a bag"></div>
      <div class="circle-photo circle-photo--inner tone-trees" role="img" aria-label="Tall pines over the course at dusk"></div>
      <div class="circle-photo tone-swing" role="img" aria-label="Golfer mid swing on the course"></div>
    </div>

    <div class="notes">
      <p>Children 15 and Under<br>Free <span class="regular">with Paid Adult</span></p>
      <p>Lunch Available Daily<br>10AM – 3PM</p>
    </div>

    <footer class="footer">The Harbors of Cedar Creek Golf Club 4410 SW<br>Heron Bay Dr Palmview, FL 30000</footer>
  </section>

  <div class="side-label side-label--front">FRONT</div>
  <div class="side-label side-label--back">BACK</div>

</body>
</html>
```